QM Regulatory Pathways - Biz Card - Re-do

I would like a re-do on my business card.

See my Internet site - qmregpathways.example

1) Remove direct phone line.
2) Add company moto - integrity, diligence, and excellence
3) Add Consulting Services listing:
-Benefit Technology
-ERISA Compliance
-Contract/Vendor Management
-Human Resource/Payroll
-Medical/Prescription Drug
-Integrated Leave of Absence

Target Market(s)

Employee benefit consulting and insurance purchasers, Usually human resource executives

Industry/Entity Type

Human Resource

Contact Information for Business Card

Same business card color scheme, logo,

Font styles to use
Sans Serif

Requirements
Must have
• Same color scheme and logo. Remove direct phone number. Keep all numbers, internet address.

```html
<!DOCTYPE html>
<html lang="en">
<head>
<meta charset="utf-8">
<title>QM Regulatory Pathways – Business Card</title>
<link href="https://fonts.googleapis.com/css2?family=Libre+Bodoni:wght@400;700&display=swap" rel="stylesheet">
<style>
  :root {
    --plum: #6b2048;
    --white: #ffffff;
    --mist: #e3e3e3;
    --ink: #333333;
    --backdrop: #d9d9d9;
  }
  * { margin: 0; padding: 0; box-sizing: border-box; }
  html, body { width: 1200px; height: 1000px; overflow: hidden; }
  body {
    background: var(--backdrop);
    font-family: "Libre Bodoni", "Times New Roman", serif;
    position: relative;
  }
  .card {
    position: absolute;
    left: 220px;
    width: 760px;
    height: 434px;
    border-radius: 26px;
    overflow: hidden;
  }

  /* Back of card */
  .card-back { top: 52px; background: var(--plum); color: var(--white); text-align: center; }
  .back-mark {
    position: absolute; left: 50%; top: 58px; transform: translateX(-50%);
    width: 92px; height: 92px; border-radius: 50%; background: var(--white);
  }
  .back-name { position: absolute; top: 168px; width: 100%; font-size: 42px; font-weight: 400; letter-spacing: 0.5px; }
  .motto { position: absolute; top: 230px; width: 100%; font-size: 19px; letter-spacing: 0.8px; }
  .motto .dot { display: inline-block; width: 9px; height: 9px; border-radius: 50%; background: var(--white); margin: 0 8px 2px; }
  .services { position: absolute; top: 300px; width: 100%; font-size: 17px; line-height: 1.55; letter-spacing: 0.3px; }
  .services span { margin: 0 14px; }

  /* Front of card */
  .card-front { top: 514px; background: var(--mist); }
  .front-shape { position: absolute; inset: 0; }
  .front-mark {
    position: absolute; left: 110px; top: 62px;
    width: 184px; height: 184px; border-radius: 50%; background: var(--plum);
  }
  .front-name {
    position: absolute; left: 40px; top: 276px; width: 324px;
    text-align: center; font-size: 27px; line-height: 1.2; color: var(--plum);
  }
  .contact { position: absolute; left: 474px; top: 150px; color: var(--ink); }
  .person { font-size: 22px; font-weight: 700; color: var(--plum); }
  .role { font-size: 16px; margin-bottom: 18px; }
  .address { font-size: 14.5px; line-height: 1.3; margin-bottom: 4px; }
  .line { display: flex; align-items: center; font-size: 14.5px; line-height: 1.45; }
  .line svg { width: 12px; height: 12px; margin-right: 7px; fill: var(--ink); flex: none; }
  .web { color: var(--plum); font-weight: 700; }
  .web svg { fill: var(--ink); }
</style>
</head>
<body>

<section class="card card-back">
  <div class="back-mark"></div>
  <h1 class="back-name">QM Regulatory Pathways</h1>
  <p class="motto">Integrity<span class="dot"></span>Diligence<span class="dot"></span>Excellence</p>
  <div class="services">
    <div><span>Benefit Technology</span><span>ERISA Compliance</span><span>Contract/Vendor Management</span></div>
    <div><span>Human Resource/Payroll</span><span>Medical/Prescription Drug</span><span>Integrated Leave of Absence</span></div>
  </div>
</section>

<section class="card card-front">
  <svg class="front-shape" viewBox="0 0 760 434" preserveAspectRatio="none">
    <path d="M0 0 H395 C470 120 450 320 330 434 H0 Z" fill="var(--plum)"/>
    <path d="M0 0 H380 C450 120 425 320 300 434 H0 Z" fill="var(--white)"/>
  </svg>
  <div class="front-mark"></div>
  <div class="front-name">QM Regulatory Pathways</div>

  <div class="contact">
    <div class="person">Dana Whitfield</div>
    <div class="role">President</div>
    <div class="address">1180 Lakeshore Drive, Suite 210<br>Harbor City, MI 49000</div>
    <div class="line">
      <svg viewBox="0 0 12 12"><path d="M2.5 0.5 L4.5 0.5 L5.2 3.2 L3.8 4.3 C4.5 5.8 6.2 7.5 7.7 8.2 L8.8 6.8 L11.5 7.5 L11.5 9.5 C11.5 10.6 10.6 11.5 9.5 11.5 C4.5 11.5 0.5 7.5 0.5 2.5 C0.5 1.4 1.4 0.5 2.5 0.5 Z"/></svg>
      555.014.2231
    </div>
    <div class="line">
      <svg viewBox="0 0 12 12"><rect x="3" y="0.5" width="6" height="3.5"/><rect x="0.5" y="4.5" width="11" height="5" rx="1"/><rect x="3" y="8.5" width="6" height="3" fill="var(--mist)" stroke="var(--ink)" stroke-width="1"/></svg>
      555.014.2232
    </div>
    <div class="line">
      <svg viewBox="0 0 12 12"><rect x="0.5" y="2" width="11" height="8" rx="1"/><path d="M1 2.8 L6 6.6 L11 2.8" stroke="var(--mist)" stroke-width="1.2" fill="none"/></svg>
      dwhitfield@qmregpathways.example
    </div>
    <div class="line web">
      <svg viewBox="0 0 12 12"><circle cx="6" cy="6" r="5.5"/><path d="M0.5 6 H11.5 M6 0.5 C3.5 3 3.5 9 6 11.5 M6 0.5 C8.5 3 8.5 9 6 11.5" stroke="var(--mist)" stroke-width="0.9" fill="none"/></svg>
      www.qmregpathways.example
    </div>
  </div>
</section>

</body>
</html>
```